Dental Hygiene Packaging Design

I am looking for packaging design for my on the go dental hygiene product. My product is a single serving tooth powder that foams in your mouth when you use it. You can swish the product around for 60 seconds like mouthwash or you can use a toothbrush to brush with it. The designs need to be focused around the fact that the product can be used while on the go. It is versatile, convenient, and effective. It can be used in any clime or place. The package designs need to be bright with vivid colors that are competitive with the current dental hygiene product color schemes on the market. It needs to pop out at you and be eye catching. The design and words need to tell you exactly what the product is. The new flavors of the tooth powder will be orange, cinnamon, and peppermint. I am looking for a universal packaging design that is easily interchangeable between the 3 flavor color schemes. Provide 3 separate designs for the 3 separate flavors if possible. The stand up pouch size is 120mm x 69mm x 125mm. I have attached a variety of logos and other necessary packaging materials. I attached a photo of my previous product packaging. DO NOT use this layout. It is only for your assistance in understanding the product. Also attached is a word document containing what was written on the previous packaging.

Target Market(s)

Outdoor Market, Camping, Hiking, Traveling, On the Go. Dental Industry, Convenience

Industry/Entity Type

Dental Hygiene

Colors
0054AA
0677BA
7BADD7
CADEEF
E8F1F8
0094D4
00A9DD
6FCCEA
C7EBF8
E9F6FB
00AB8E
00BBA5
67D7C9
C6EFE9
E9F9F6
59FF00
82FF00
B8FF75
E3FFCB
F4FFEA
FFF300
FFF600
FEFA6F
FFFEC7
FFFEE8
FFC000
F8CF3A
FAE287
FDF2CF
FEFAEE
F0912C
F2A743
F7CA91
FBE8D2
FDF5EE
EE7325
F08F49
F5BC92
FAE3D3
FDF4ED
EB3D1F
EC4F4E
F09395
F8D3D4
FCEDEE

Requirements
Must have
• Veteran Owned stamp, organic stamp. Try to keep the same items on the new design that were on the old one.
Nice to have
• Be innovative and add something you think will make your design stand out more.

```html
<!DOCTYPE html>
<html lang="en">
<head>
<meta charset="utf-8">
<title>TRAILDENT Peppermint Pouch</title>
<link rel="stylesheet" href="https://fonts.googleapis.com/css2?family=Roboto+Condensed:wght@400;700;800&display=swap">
<style>
  :root {
    --stage-green: #43901f;
    --band-green: #4e9f29;
    --band-green-dark: #3f8a1e;
    --kraft-cream: #e4ddd0;
    --lime: #b3cc3a;
    --flavor-ink: #1e560d;
    --brand-brown: #3b1d12;
    --paper-white: #f4f1ea;
    --leaf-light: #c6dc5a;
    --leaf-mid: #5fae36;
  }
  * { box-sizing: border-box; margin: 0; padding: 0; }
  html, body { width: 1200px; height: 705px; overflow: hidden; }
  body {
    background: var(--stage-green);
    font-family: "Roboto Condensed", "Arial Narrow", sans-serif;
    position: relative;
  }
  .pouch {
    position: absolute;
    left: 205px;
    top: 108px;
    width: 860px;
    height: 640px;
    background: var(--kraft-cream);
    overflow: hidden;
    border-radius: 4px;
  }
  .tagline-band {
    position: absolute;
    left: 0; top: 0;
    width: 100%;
    height: 78px;
    background: var(--band-green);
    display: flex;
    align-items: center;
    padding-left: 80px;
  }
  .tooth-badge {
    position: absolute;
    left: 78px; top: 30px;
    width: 76px; height: 86px;
    border-radius: 26px 26px 34px 34px;
    background: var(--band-green);
    border: 5px solid var(--paper-white);
  }
  .tagline {
    margin-left: 90px;
    margin-top: 14px;
    color: var(--paper-white);
    font-weight: 800;
    font-size: 35px;
    letter-spacing: 0.5px;
    white-space: nowrap;
  }
  .brand {
    position: absolute;
    left: 110px; top: 215px;
    display: flex;
    align-items: center;
    gap: 16px;
  }
  .brand-dot {
    width: 34px; height: 34px;
    border-radius: 50%;
    background: var(--brand-brown);
  }
  .brand-name {
    color: var(--brand-brown);
    font-weight: 800;
    font-size: 84px;
    letter-spacing: 1px;
    line-height: 1;
  }
  .leaf-art {
    position: absolute;
    right: 30px; top: 150px;
    width: 290px; height: 500px;
    border-radius: 140px 140px 0 0;
    background: linear-gradient(160deg, var(--leaf-mid) 0%, var(--leaf-light) 55%, var(--leaf-mid) 100%);
    opacity: 0.85;
  }
  .flavor-band {
    position: absolute;
    left: 0; top: 405px;
    width: 570px; height: 115px;
    background: var(--lime);
    border-radius: 0 24px 0 0;
  }
  .flavor-name {
    position: absolute;
    left: 75px; top: 422px;
    color: var(--flavor-ink);
    font-weight: 800;
    font-size: 84px;
    line-height: 1;
    letter-spacing: 0.5px;
  }
  .story-band {
    position: absolute;
    left: 0; top: 520px;
    width: 570px; height: 140px;
    background: var(--band-green-dark);
    padding: 14px 0 0 75px;
    color: var(--paper-white);
  }
  .story-headline {
    font-size: 21px;
    font-weight: 400;
    letter-spacing: 0.3px;
    white-space: nowrap;
  }
  .story-body {
    margin-top: 4px;
    font-size: 19px;
    line-height: 1.2;
    opacity: 0.8;
    width: 470px;
  }
</style>
</head>
<body>
  <main class="pouch">
    <header class="tagline-band">
      <p class="tagline">CLEAN YOUR TEETH ANYTIME, ANYWHERE</p>
    </header>
    <div class="tooth-badge" role="img" aria-label="Tooth icon with sparkles"></div>

    <div class="brand">
      <span class="brand-name">TRAILDENT</span>
      <span class="brand-dot"></span>
    </div>

    <div class="leaf-art" role="img" aria-label="Scattered peppermint leaves illustration"></div>

    <div class="flavor-band"></div>
    <h1 class="flavor-name">PEPPERMINT</h1>

    <section class="story-band">
      <p class="story-headline">TRAILDENT IS NOT JUST A PRODUCT, IT'S A MOVEMENT!</p>
      <p class="story-body">It is 100% all natural and vegan friendly, gluten free. It's a great way to keep your smile fresh.</p>
    </section>
  </main>
</body>
</html>
```